Pause Often, Now Discover Poster for Fernvale Stacks Keepers

Task Description
I am the Vice President of Advocacy for the Fernvale Stacks Keepers Association. I am looking to have a set of posters made for POND (Pause Often, Now Discover) in October. POND is a time when all school children in BC are encouraged to Pause Often, Now Discover for 15-20 minutes at some point in their day.

I would like to get a set of 2 digital posters designed (if possible it would be nice to have the option to print to both 11x17 and 8.5x 11 paper). We need a poster that is high school (Grade 8-12) appropriate and one that is elementary (Grade k-7) appropriate. Both posters need to be replicated in French. All posters need to have the FOMU logo on them as well as the Fernvale Stacks Keepers Association Logo.

My budget is not huge (whose is?), but we are flexible and open with design. We want posters that appeal to the age groups they are designed for and that promote reading. We would require the digital copy by August 20. Schools will arrange for their own printing as distribution to all the schools in BC is laborious.

Each poster needs to have the following information:

-Pause Often, Now Discover (POND)
- A Blank Spot that we can add a date to
-the logo for the FOMU (attached)
-the logo for the FSKA (attached)- the logos do not have to be large.

Industry/Entity Type

Teacher

Font styles to use
Serif

Requirements
Must have
• -Pause Often, Now Discover (POND)
• - A Blank Spot that we can add a date to
• -the logo for the FOMU (attached)
• -the logo for the FSKA (attached)- the logos do not have to be large.
Nice to have
• Clear Bright Colours
• I have attached last year's posters to give an idea of what we are interested in.

```html
<!DOCTYPE html>
<html lang="en">
<head>
<meta charset="utf-8">
<title>Pause Often, Now Discover — Fernvale Stacks Keepers Association</title>
<link rel="stylesheet" href="https://fonts.googleapis.com/css2?family=Michroma&family=Graduate&family=Oswald:wght@500;700&family=Open+Sans:wght@400;700&family=Libre+Baskerville:wght@700&display=swap">
<style>
  :root {
    --green-deep: #2f8f2c;
    --green-mid: #3ea53a;
    --green-light: #62c04f;
    --ink: #111111;
    --silver-light: #f2f2f2;
    --silver-dark: #8c8c8c;
    --white: #ffffff;
    --name-green: #3fb13a;
    --photo-warm: #8a5a32;
    --photo-cool: #2f6fb0;
  }
  * { margin: 0; padding: 0; box-sizing: border-box; }
  html, body { width: 907px; height: 1200px; overflow: hidden; background: #ffffff; }
  .poster {
    position: relative;
    width: 907px;
    height: 1200px;
    overflow: hidden;
    background: linear-gradient(100deg, var(--green-deep) 0%, var(--green-mid) 45%, var(--green-light) 100%);
    font-family: "Open Sans", sans-serif;
  }
  .hero-photo {
    position: absolute;
    left: 0; top: 0;
    width: 907px; height: 620px;
    background:
      radial-gradient(ellipse at 30% 55%, rgba(47,111,176,0.85) 0%, rgba(47,111,176,0) 35%),
      radial-gradient(ellipse at 85% 50%, rgba(25,25,25,0.85) 0%, rgba(25,25,25,0) 40%),
      linear-gradient(180deg, #6b4124 0%, var(--photo-warm) 50%, #b07a4b 100%);
  }
  .bands { position: absolute; left: 0; top: 0; width: 907px; height: 1200px; }
  .brand-banner {
    position: absolute;
    left: 0; top: 0;
    width: 345px; height: 330px;
    background: linear-gradient(180deg, #ffffff 0%, #e9e9e9 100%);
    clip-path: polygon(0 0, 100% 0, 100% 82%, 0 100%);
    display: flex;
    align-items: center;
    justify-content: center;
    padding-bottom: 40px;
  }
  .brand-name {
    font-family: "Libre Baskerville", serif;
    font-weight: 700;
    font-size: 78px;
    color: var(--ink);
    letter-spacing: 2px;
  }
  .headline {
    position: absolute;
    left: 38px; top: 630px;
    color: var(--white);
  }
  .headline-lead {
    display: block;
    font-family: "Michroma", sans-serif;
    font-size: 92px;
    line-height: 1;
    letter-spacing: 2px;
  }
  .headline-rest {
    display: block;
    margin-top: 22px;
    font-family: "Graduate", serif;
    font-size: 57px;
    line-height: 1;
    color: var(--ink);
    white-space: nowrap;
  }
  .date-bar {
    position: absolute;
    left: 36px; top: 858px;
    width: 830px; height: 54px;
    border-radius: 10px;
    background: linear-gradient(180deg, #2a2a2a, #000000);
    border: 3px solid #d6d6d6;
    display: flex;
    align-items: center;
    justify-content: center;
    font-family: "Michroma", sans-serif;
    font-size: 25px;
    color: var(--white);
    white-space: nowrap;
  }
  .partner-mark {
    position: absolute;
    left: 52px; top: 972px;
    width: 118px; height: 118px;
    border-radius: 50%;
    border: 3px solid var(--ink);
    display: flex;
    align-items: center;
    justify-content: center;
    font-family: "Libre Baskerville", serif;
    font-weight: 700;
    font-size: 28px;
    color: var(--ink);
  }
  .call-line {
    position: absolute;
    left: 242px; top: 960px;
    display: flex;
    align-items: baseline;
    gap: 18px;
    font-family: "Oswald", sans-serif;
    font-weight: 700;
  }
  .call-label { font-size: 42px; color: var(--ink); font-weight: 500; }
  .call-number { font-size: 70px; color: var(--white); letter-spacing: 1px; }
  .contact {
    position: absolute;
    left: 0; top: 1128px;
    width: 1040px;
    text-align: center;
    line-height: 1.35;
  }
  .contact-name { font-weight: 700; font-size: 23px; color: var(--name-green); }
  .contact-address { font-size: 18px; color: var(--white); word-spacing: 2px; }
</style>
</head>
<body>
<main class="poster">
  <div class="hero-photo" role="img" aria-label="Photo: students and a teacher reading together in front of library bookshelves"></div>

  <svg class="bands" viewBox="0 0 907 1200" aria-hidden="true">
    <defs>
      <linearGradient id="silver" x1="0" y1="0" x2="1" y2="0">
        <stop offset="0" stop-color="#9a9a9a"/>
        <stop offset="0.5" stop-color="#f5f5f5"/>
        <stop offset="1" stop-color="#8c8c8c"/>
      </linearGradient>
      <linearGradient id="green-fill" x1="0" y1="0" x2="1" y2="0">
        <stop offset="0" stop-color="#2f8f2c"/>
        <stop offset="0.45" stop-color="#3ea53a"/>
        <stop offset="1" stop-color="#62c04f"/>
      </linearGradient>
    </defs>
    <!-- top divider -->
    <polygon class="green-field" fill="url(#green-fill)" points="0,400 590,610 907,525 907,1200 0,1200"/>
    <polygon class="divider-black" fill="#111" points="0,372 590,582 907,498 907,545 590,640 0,412"/>
    <polygon class="divider-silver" fill="url(#silver)" points="0,330 590,550 907,462 907,500 590,586 0,374"/>
    <polygon class="divider-white" fill="#ffffff" points="0,320 590,540 907,452 907,462 590,550 0,330"/>
    <!-- bottom divider and footer -->
    <polygon class="footer-silver" fill="url(#silver)" points="0,1100 560,1035 907,1100 907,1125 560,1062 0,1125"/>
    <polygon class="footer-white" fill="#ffffff" points="0,1125 560,1062 907,1125 907,1132 560,1070 0,1132"/>
    <polygon class="footer-black" fill="#111" points="0,1132 560,1070 907,1132 907,1200 0,1200"/>
  </svg>

  <div class="brand-banner">
    <span class="brand-name">FSKA</span>
  </div>

  <h1 class="headline">
    <span class="headline-lead">PAUSE</span>
    <span class="headline-rest">OFTEN, NOW DISCOVER</span>
  </h1>

  <div class="date-bar">A BLANK SPOT THAT WE CAN ADD A DATE</div>

  <div class="partner-mark">FOMU</div>

  <p class="call-line">
    <span class="call-label">CALL NOW</span>
    <span class="call-number">0198765432</span>
  </p>

  <address class="contact">
    <span class="contact-name">Marion Teller</span><br>
    <span class="contact-address">218-12B Lane &nbsp; Fernvale, BC &nbsp;V0X 2K7</span>
  </address>
</main>
</body>
</html>
```